Kovaridex Website

we need a web site similar to Zumwarp.com or Ostrix9 com or brackfield.com - Although our budget is small we would like to look like them. we are in the same industry
Reason: Can you do an exact copy of Zumwarp.com if so how long ? What do you require? What is the next step?Please let me know you can also email me at tolvaburn@pexmail.com for faster answers.
Thank you
Target Market(s)
small and medium size business
Requirements
Must have
- product portfolio - just like Zumwarp.com
Nice to have
- ecomerce and mobile app

```html
<!DOCTYPE html>
<html lang="en">
<head>
<meta charset="utf-8">
<title>Kovaridex</title>
<link href="https://fonts.googleapis.com/css2?family=Signika:wght@300;400;600&display=swap" rel="stylesheet">
<style>
:root{
  --blue:#2aa3df;
  --blue-dark:#1a8cc8;
  --blue-light:#4dbdf0;
  --ink:#3c3c3c;
  --text:#5a5a5a;
  --muted:#777;
  --line:#d6d6d6;
  --hero:#f2f2f2;
  --footer:#f3f3f3;
  --green:#7cb518;
  --red:#ea4a2e;
  --orange:#f7a51a;
}
*{margin:0;padding:0;box-sizing:border-box}
html,body{width:1025px;height:1200px;overflow:hidden;background:#fff}
body{font-family:"Signika",sans-serif;font-weight:300;color:var(--text);position:relative}
.abs{position:absolute}
.top-rule{left:0;top:0;width:1025px;height:4px;background:#e6e6e6}
.util-links{right:67px;top:12px;font-size:12px;color:var(--muted)}
.util-links span{margin:0 4px;color:#999}
.brand{left:58px;top:44px;display:flex;align-items:center;gap:8px}
.brand-dot{width:34px;height:34px;border-radius:50%;background:var(--blue)}
.brand-name{font-size:34px;font-weight:300;color:var(--blue);letter-spacing:.5px}
.search{left:738px;top:59px;width:222px;height:29px;border:1px solid #ccc;background:#fff;font-size:11px;font-style:italic;color:#999;padding:7px 11px}
.search svg{position:absolute;right:10px;top:7px}
.nav{left:0;top:106px;width:1025px;height:45px;background:linear-gradient(#4cc0f2,#1f9ad9);border-bottom:1px solid #1580bf}
.nav a{position:absolute;top:14px;font-size:15px;color:#fff;text-decoration:none;font-weight:400}
.nav i{position:absolute;top:0;width:1px;height:45px;background:#1e86c2;box-shadow:1px 0 0 #5ccaf5}
.hero{left:0;top:152px;width:1025px;height:327px;background:linear-gradient(#fff,var(--hero));border-bottom:1px solid #e4e4e4}
.hero h1{position:absolute;left:86px;top:54px;font-size:30px;font-weight:300;color:var(--ink);line-height:1.2}
.hero h2{position:absolute;left:85px;top:92px;font-size:42px;font-weight:300;color:var(--blue);line-height:1.2}
.hero p{position:absolute;left:86px;top:140px;width:400px;font-size:12.5px;line-height:22px;color:var(--text)}
.btn-dark{position:absolute;left:87px;top:191px;width:93px;height:28px;background:linear-gradient(#777,#4b4b4b);border-radius:3px;color:#fff;font-size:12.5px;font-weight:400;text-align:center;line-height:28px}
.dots{position:absolute;left:87px;top:237px;display:flex;gap:4px}
.dots b{width:12px;height:12px;border-radius:50%;background:#666}
.dots b:first-child{background:var(--blue)}
.hero-art{position:absolute;left:550px;top:21px;width:354px;height:266px;border-radius:8px;background:radial-gradient(ellipse at 55% 35%,#bfe5f8,#e6f2f8 55%,#f4f5f6 80%)}
.sec-title{font-size:23px;font-weight:300;color:var(--ink)}
.product{width:140px;text-align:center}
.product .icon{width:72px;height:72px;border-radius:50%;margin:0 auto;display:flex;align-items:center;justify-content:center}
.product h3{font-size:14px;font-weight:400;margin-top:12px}
.product p{font-size:11px;line-height:17px;margin-top:3px;color:var(--text)}
.blog{left:698px;top:549px;width:270px}
.blog h4{font-size:12.5px;font-weight:400;color:#222}
.blog p{font-size:12px;line-height:18px;color:var(--text);margin-bottom:14px}
.divider{left:60px;top:734px;width:907px;height:14px;background:radial-gradient(ellipse at center,#ececec,#fff 70%)}
.about{left:62px;top:813px;width:278px;font-size:12px;line-height:19.5px;color:var(--text);text-align:justify}
.about p+p{margin-top:9px}
.btn-blue{left:62px;top:986px;width:102px;height:29px;background:linear-gradient(#4dc0f2,#1f98d6);border-radius:2px;color:#fff;font-size:12px;font-weight:600;text-align:center;line-height:29px}
.quote{left:380px;top:811px;width:276px;height:166px;border-radius:14px;background:linear-gradient(#f4f4f4,#e4e4e4);border:1px solid #e0e0e0;padding:16px 18px 0 32px}
.quote p{font-size:11px;font-style:italic;line-height:21.3px;color:var(--text)}
.quote .mark{position:absolute;left:13px;top:12px;font-size:26px;font-weight:600;color:#555;line-height:1}
.quote .by{font-size:12px;color:#444;margin-top:7px;font-weight:400}
.video{left:696px;top:811px;width:271px;height:178px;background:linear-gradient(135deg,#4a5058,#2a2d33)}
.play{position:absolute;left:120px;top:73px;width:32px;height:32px;border-radius:50%;background:#111;border:2px solid #fff}
.footer{left:0;top:1062px;width:1025px;height:138px;background:linear-gradient(#ececec,var(--footer) 20%)}
.foot-links{position:absolute;left:58px;top:38px;font-size:12.5px;color:#222;font-weight:400}
.foot-links span{margin:0 4px;color:#555}
.copy{position:absolute;left:58px;top:64px;font-size:12px;color:#444}
.social{position:absolute;left:840px;top:33px;display:flex;gap:9px}
.social b{width:24px;height:24px;border-radius:2px}
</style>
</head>
<body>
<div class="abs top-rule"></div>
<div class="abs util-links">Customer Center <span>|</span> Careers <span>|</span> Blog <span>|</span> Partner <span>|</span> Contact Us</div>
<div class="abs brand"><span class="brand-dot"></span><span class="brand-name">KOVARIDEX</span></div>
<div class="abs search">Search here..
  <svg width="15" height="15" viewBox="0 0 15 15"><circle cx="6" cy="6" r="4.5" fill="none" stroke="#666" stroke-width="2"/><line x1="9.5" y1="9.5" x2="13.5" y2="13.5" stroke="#666" stroke-width="2.4"/></svg>
</div>

<nav class="abs nav">
  <a style="left:83px">HOME</a><i style="left:148px"></i>
  <a style="left:175px">SERVICES</a><i style="left:260px"></i>
  <a style="left:285px">PRODUCTS</a><i style="left:380px"></i>
  <a style="left:408px">ABOUT US</a><i style="left:496px"></i>
  <a style="left:525px">SOLUTIONS</a><i style="left:622px"></i>
  <a style="left:650px">RESOURCES</a><i style="left:748px"></i>
  <a style="left:778px">WHY CHOOSE US</a>
</nav>

<section class="abs hero">
  <h1>We Provide Our Customers</h1>
  <h2>Clouds Products</h2>
  <p>Vivamus porttitor, g, purus nisi eleifend libero, a tempus libero lectus feugiat felis. Morbi diam mauris, viverra in, gravida eu, mattis</p>
  <div class="btn-dark">Learn More</div>
  <div class="dots"><b></b><b></b><b></b><b></b></div>
  <div class="hero-art" role="img" aria-label="Illustration of a cloud connected to several laptops"></div>
</section>

<h2 class="abs sec-title" style="left:62px;top:508px">Products We Provide</h2>
<div class="abs product" style="left:54px;top:554px">
  <div class="icon" style="background:radial-gradient(circle at 40% 35%,#9fd43a,var(--green))">
    <svg width="40" height="40" viewBox="0 0 40 40" fill="none" stroke="#fff" stroke-width="2"><circle cx="20" cy="20" r="14"/><ellipse cx="20" cy="20" rx="6" ry="14"/><line x1="6" y1="20" x2="34" y2="20"/></svg>
  </div>
  <h3 style="color:var(--green)">Product Name</h3>
  <p>Gravida eu, mattis in, ante. Morbi eget arcu Morbi porta</p>
</div>
<div class="abs product" style="left:212px;top:554px">
  <div class="icon" style="background:radial-gradient(circle at 40% 35%,#f8735a,var(--red))">
    <svg width="40" height="40" viewBox="0 0 40 40" stroke="#fff" stroke-width="1.6" fill="#fff"><line x1="20" y1="20" x2="8" y2="8"/><line x1="20" y1="20" x2="32" y2="8"/><line x1="20" y1="20" x2="10" y2="30"/><line x1="20" y1="20" x2="30" y2="32"/><circle cx="20" cy="20" r="3.5"/><circle cx="8" cy="8" r="2.5"/><circle cx="32" cy="8" r="2.5"/><circle cx="10" cy="30" r="2.5"/><circle cx="30" cy="32" r="2.5"/></svg>
  </div>
  <h3 style="color:var(--red)">Product Name</h3>
  <p>Gravida eu, mattis in, ante. Morbi eget arcu Morbi porta</p>
</div>
<div class="abs product" style="left:366px;top:554px">
  <div class="icon" style="background:radial-gradient(circle at 40% 35%,#ffc93c,var(--orange))">
    <svg width="44" height="40" viewBox="0 0 44 40" fill="none" stroke="#fff" stroke-width="2.2"><path d="M12 30h-2a8 8 0 0 1 0-16 11 11 0 0 1 21-2 8 8 0 0 1 3 18h-2"/><path d="M22 34V18M16 23l6-6 6 6"/></svg>
  </div>
  <h3 style="color:var(--orange)">Product Name</h3>
  <p>Gravida eu, mattis in, ante. Morbi eget arcu Morbi porta</p>
</div>
<div class="abs product" style="left:521px;top:554px">
  <div class="icon" style="background:radial-gradient(circle at 40% 35%,#5fc8f5,var(--blue-dark))">
    <svg width="34" height="34" viewBox="0 0 34 34"><path d="M11 4l4 7-3 3c1 4 4 7 8 9l3-3 7 4-3 5c-10 0-22-12-21-23z" fill="#fff"/></svg>
  </div>
  <h3 style="color:var(--blue)">Product Name</h3>
  <p>Gravida eu, mattis in, ante. Morbi eget arcu Morbi porta</p>
</div>

<h2 class="abs sec-title" style="left:696px;top:508px">Recent Blog Post</h2>
<div class="abs blog">
  <h4>Eu mattis in ante</h4>
  <p>Vivamus sollicitudin metus eget eros.</p>
  <h4>Morbi eget arcu</h4>
  <p>Mauris vel lacus vitae felis vestibulum volutpat</p>
  <h4>Nulla elementum dui ut</h4>
  <p>Lorem ipsum dolor sit amet, consectetuer adipisc ing elit. Nam cursus. Morbi ut mi.</p>
</div>

<div class="abs divider"></div>

<h2 class="abs sec-title" style="left:62px;top:774px">About Our Company</h2>
<div class="abs about">
  <p>Duis tincidunt lectus quis dui viverra vestibulum. Suspendisse vulputate aliquam dui. Nulla elementum dui ut augue. Aliquam vehicula mi at mauris. Maecenas placerat, nisl at consequat rhoncus, sem nunc gravida justo, quis eleifend arcu velit quis lacus.</p>
  <p>Morbi magna magna, tincidunt a, mattis non, imperdiet vitae, tellus. Sed odio est, auctor ac, sollicitudin in, consequat vitae, orci. Fusce id felis.</p>
</div>
<div class="abs btn-blue">LEARN MORE</div>

<h2 class="abs sec-title" style="left:381px;top:774px;color:var(--blue)">What Our Customer Says</h2>
<div class="abs quote">
  <span class="mark">“</span>
  <p>Phasellus felis dolor, scelerisque a, tempus eget, lobortis id, libero. Donec scelerisque leo ac risus. Praesent sit amet est. In dictum, dolor eu dictum porttitor, enim felis viverra mi, eget luctus massa purus quis odio Etiam nulla massa <b style="font-style:normal">”</b></p>
  <div class="by">By Author Name</div>
</div>

<h2 class="abs sec-title" style="left:693px;top:774px">Watch Our Video</h2>
<div class="abs video" role="img" aria-label="Video still of a person sketching cloud diagrams on a chalkboard">
  <span class="play"><svg width="28" height="28" viewBox="0 0 28 28"><path d="M11 8l9 6-9 6z" fill="#fff"/></svg></span>
</div>

<footer class="abs footer">
  <div class="foot-links">HOME <span>|</span> SERVICES <span>|</span> PRODUCTS <span>|</span> ABOUT US <span>|</span> SOLUTIONS <span>|</span> RESOURCES <span>|</span> WHY CHOOSE US <span>|</span> CONTACT</div>
  <div class="copy">© 2013 Company Name.&nbsp; All right reserved.&nbsp; Term of Use</div>
  <div class="social"><b style="background:#3b5a98"></b><b style="background:#4cc3ef"></b><b style="background:#1a7bb9"></b><b style="background:#f08a1c"></b></div>
</footer>
</body>
</html>
```